Government contracting small business needs a web design

Tarnvale Systems Inc is a veteran owned small business that delivers a full range of professional services as well as training in information technology, security and defense intelligence solutions.
We need a professional/corporate looking website where potential clients can view what services are offered.
This being a new company, there is not much that can added more than a narrative statement, stock photos and a place where potential customers and employees can make contact.
Open to ideas.
US Government
Small Business

```html
<!DOCTYPE html>
<html lang="en">
<head>
<meta charset="utf-8">
<title>Tarnvale Systems Inc</title>
<link rel="stylesheet" href="https://fonts.googleapis.com/css2?family=Arimo:wght@400;700&family=PT+Sans+Narrow:wght@400;700&family=PT+Sans:wght@400;700&family=Kalam:wght@400&display=swap">
<style>
:root{
  --yellow:#f4c51c;
  --yellow-dark:#e4b40f;
  --ink:#1a1a1a;
  --heading:#4a4a4a;
  --panel:#555555;
  --panel-edge:#d9d9d9;
  --field:#3f3f3f;
  --hero-black:#050505;
  --hero-photo:#3a0a06;
  --step-label:#c5cad8;
  --footer:#ebebeb;
  --white:#ffffff;
}
*{margin:0;padding:0;box-sizing:border-box}
html,body{width:925px;height:1200px;overflow:hidden;background:var(--white)}
body{position:relative;font-family:"PT Sans",Arial,sans-serif;color:var(--ink)}
.abs{position:absolute}

.brand{left:20px;top:26px;display:flex;align-items:center;gap:6px;font-family:"Arimo",Arial,sans-serif;font-weight:700;font-size:21px;color:var(--ink);letter-spacing:-.3px}
.brand-dot{width:32px;height:32px;border-radius:50%;background:var(--ink)}
.search{left:693px;top:31px;width:212px;height:22px;border:1px solid #d8d8d8;border-radius:4px;background:linear-gradient(#f3f3f3,#fafafa)}
.search svg{position:absolute;right:9px;top:5px}

.main-nav{left:9px;top:69px;width:907px;height:38px;background:linear-gradient(#f8d23a,var(--yellow) 60%,var(--yellow-dark));border:1px solid #f0dc8a;display:flex;list-style:none}
.main-nav li{font-family:"Arimo",Arial,sans-serif;font-weight:700;font-size:10px;color:var(--ink);line-height:38px;padding:0 20px 0 29px;border-right:1px solid rgba(0,0,0,.12)}
.main-nav li:first-child{padding-left:29px;padding-right:22px}
.main-nav li:last-child{border-right:0}

.hero{left:9px;top:114px;width:905px;height:311px;background:var(--hero-black)}
.hero-photo{position:absolute;left:0;top:0;width:524px;height:311px;background:radial-gradient(ellipse at 45% 50%,#7a1e0e 0%,var(--hero-photo) 55%,#120303 100%)}
.hero h1{position:absolute;left:539px;top:102px;font-family:"Arimo",Arial,sans-serif;font-weight:700;font-size:50px;line-height:44px;color:var(--white);letter-spacing:-1px}
.hero p{position:absolute;left:546px;top:206px;width:340px;font-family:"Arimo",Arial,sans-serif;font-weight:700;font-size:12px;line-height:16px;color:var(--white)}

.steps{left:9px;top:426px;width:905px;height:70px}
.step-label{position:absolute;top:46px;font-family:"PT Sans Narrow",sans-serif;font-size:15px;color:var(--step-label);text-transform:uppercase;transform:translateX(-50%)}
.step-label.current{color:#4a4a4a}

.panel{left:9px;top:514px;width:906px;height:334px;background:var(--panel);border:2px solid var(--panel-edge)}
.panel h2{position:absolute;top:26px;font-family:"PT Sans Narrow",sans-serif;font-weight:400;font-size:21px;color:var(--white);text-transform:uppercase}
.feat-title{position:absolute;left:30px;width:310px;font-family:"PT Sans Narrow",sans-serif;font-weight:700;font-size:16px;line-height:19px;color:var(--white)}
.feat-text{position:absolute;left:30px;width:310px;font-size:10px;line-height:12.5px;color:var(--white)}
.news-date{position:absolute;left:373px;font-family:"Kalam",cursive;font-size:15px;color:var(--yellow)}
.news-text{position:absolute;left:373px;width:205px;font-size:10.5px;line-height:12.5px;color:var(--white)}
.news-lead{position:absolute;left:611px;top:72px;width:275px;font-family:"PT Sans Narrow",sans-serif;font-weight:700;font-size:12px;line-height:14.5px;color:var(--white)}
.field{position:absolute;left:613px;width:220px;height:29px;background:var(--field);box-shadow:inset 0 0 6px rgba(0,0,0,.5);font-size:9px;color:#e8e8e8;line-height:27px;padding-left:17px}
.btn{position:absolute;width:98px;height:27px;background:var(--yellow);font-family:"PT Sans Narrow",sans-serif;font-size:12px;color:var(--white);text-transform:uppercase;text-align:center;line-height:27px}

.intro h2{font-family:"PT Sans Narrow",sans-serif;font-weight:700;color:var(--heading);font-size:21px}
.intro p{font-size:10.5px;line-height:12.5px;color:var(--ink)}
.welcome{left:23px;top:878px;width:410px}
.mission{left:457px;top:891px;width:450px}
.intro p+p{margin-top:13px}
.intro h2{margin-bottom:14px}

.site-footer{left:0;top:1060px;width:925px;height:140px;background:var(--footer)}
.foot-col{position:absolute;top:32px;list-style:none;font-size:11px;color:#333}
.foot-col li{height:22px}
.foot-col li:first-child{font-weight:700;font-size:12.5px;color:#333}
.copyright{position:absolute;left:616px;top:99px;font-size:10.5px;color:var(--ink)}
</style>
</head>
<body>

<header>
  <div class="brand abs"><span class="brand-dot"></span>Tarnvale Systems</div>
  <div class="search abs">
    <svg width="12" height="12" viewBox="0 0 12 12"><circle cx="4.5" cy="4.5" r="3" fill="none" stroke="#222" stroke-width="1.6"/><line x1="7" y1="7" x2="11" y2="11" stroke="#222" stroke-width="2"/></svg>
  </div>
  <ul class="main-nav abs">
    <li>HOME</li><li>INNOVATION</li><li>OUR COMPANY</li><li>INVESTORS</li><li>SERVICES</li><li>NEWSROOM</li><li>CAREERS</li><li>CONTACT</li>
  </ul>
</header>

<section class="hero abs">
  <div class="hero-photo" role="img" aria-label="Stock photo: red 3D word cloud around the word Knowledge with business terms"></div>
  <h1>Powerful &amp;<br>effective</h1>
  <p>Praesent vestibulum molestie lacus. Aenean nonummy hendrerit mauris. Phasellus porta. Fusce suscipit varius mi.</p>
</section>

<div class="steps abs">
  <svg width="905" height="40" viewBox="0 0 905 40">
    <rect x="0" y="14" width="905" height="6" rx="3" fill="#f1f1f3" stroke="#e2e2e6"/>
    <g fill="#f4f4f6" stroke="#e0e0e4">
      <circle cx="81" cy="18" r="15"/><circle cx="324" cy="18" r="15"/><circle cx="567" cy="18" r="15"/><circle cx="803" cy="18" r="15"/>
    </g>
    <circle cx="804" cy="19" r="8" fill="var(--yellow)" stroke="#e0a800"/>
  </svg>
  <span class="step-label" style="left:82px">Experience</span>
  <span class="step-label" style="left:324px">Solutions</span>
  <span class="step-label" style="left:567px">Strategies</span>
  <span class="step-label current" style="left:798px">Success</span>
</div>

<section class="panel abs">
  <h2 style="left:30px">Featured</h2>
  <h3 class="feat-title" style="top:71px">Phasellus porta. Fusce suscipit varius mi. Cum sociis natoque penatibus et magnis dis parturient montes.</h3>
  <p class="feat-text" style="top:121px">Nascetur ridiculus mus. Nulla dui. Fusce feugiat malesuada odio. Morbi nunc odio, gravida at, cursus nec, luctus a, lorem. Maecenas tristique orci ac sem. Duis ultricies pharetra magna.</p>
  <h3 class="feat-title" style="top:180px">Phasellus porta. Fusce suscipit varius mi. Cum sociis natoque penatibus et magnis dis parturient montes.</h3>
  <p class="feat-text" style="top:230px">Nascetur ridiculus mus. Nulla dui. Fusce feugiat malesuada odio. Morbi nunc odio, gravida at, cursus nec, luctus a, lorem. Maecenas tristique orci ac sem. Duis ultricies pharetra magna.</p>
  <span class="btn" style="left:227px;top:285px">Read more</span>

  <h2 style="left:373px">News &amp; Events</h2>
  <span class="news-date" style="top:70px">Jun 19, 2012</span>
  <p class="news-text" style="top:97px">Phasellus porta. Fusce suscipit varius mi. Cum sociis natoque penatibus et magnis dis parturient montes, nascetur.</p>
  <span class="news-date" style="top:178px">Jun 19, 2012</span>
  <p class="news-text" style="top:205px">Phasellus porta. Fusce suscipit varius mi. Cum sociis natoque penatibus et magnis dis parturient montes, nascetur.</p>
  <span class="btn" style="left:471px;top:285px">Read more</span>

  <h2 style="left:609px">Newsletter Sign Up</h2>
  <p class="news-lead">Phasellus porta. Fusce suscipit varius mi. Cum sociis natoque penatibus et magnis dis parturient montes.</p>
  <div class="field" style="top:115px">your name</div>
  <div class="field" style="top:152px">email id</div>
  <div class="field" style="top:188px">phone number</div>
  <span class="btn" style="left:733px;top:230px">Sign up!</span>
</section>

<section class="intro welcome abs">
  <h2>Welcome</h2>
  <p>Phasellus porta. Fusce suscipit varius mi. Cum sociis natoque penatibus et magnis dis parturient montes, nascetur ridiculus mus. Nulla dui. Fusce feugiat malesuada odio. Morbi nunc odio, gravida at, cursus nec, luctus a, lorem.<br>Maecenas tristique orci ac sem. Duis ultricies pharetra magna.</p>
  <p>Donec accumsan maada orci. Donec sit amet eros. Lorem ipsum dolor sit amet, consectetuer adipiscing elit.</p>
</section>

<section class="intro mission abs">
  <h2>Our work is dedicated to the prosperity of our clients!</h2>
  <p>Phasellus porta. Fusce suscipit varius mi. Cum sociis natoque penatibus et magnis dis parturient montes, nascetur ridiculus mus. Nulla dui. Fusce feugiat malesuada odio. Morbi nunc odio, gravida at, cursus nec, luctus a, lorem. Maecenas tristique orci ac sem. Duis ultricies pharetra magna.</p>
  <p>Donec accumsan maada orci. Donec sit amet eros. Lorem ipsum dolor sit amet, consectetuer adipiscing elit.</p>
</section>

<footer class="site-footer abs">
  <ul class="foot-col" style="left:34px"><li>About us</li><li>Who we are</li><li>Our people</li><li>Careers</li></ul>
  <ul class="foot-col" style="left:133px"><li>About us</li><li>Who we are</li><li>Our people</li><li>Careers</li></ul>
  <ul class="foot-col" style="left:224px"><li>About us</li><li>Who we are</li><li>Our people</li><li>Careers</li></ul>
  <ul class="foot-col" style="left:314px"><li>About us</li><li>Who we are</li><li>Our people</li><li>Careers</li></ul>
  <ul class="foot-col" style="left:404px"><li>About us</li><li>Who we are</li><li>Our people</li><li>Careers</li></ul>
  <ul class="foot-col" style="left:495px"><li>About us</li><li>Who we are</li><li>Our people</li><li>Careers</li></ul>
  <p class="copyright">Tarnvale Systems © 2012 | Privacy Policy</p>
</footer>

</body>
</html>
```